Driving-coach/trainer who wants to inform about the offer and how I can help people to drive more re

I need a flyer that informs potential customers about my offer.

DL size 210 mm x 99 mm, vertical!

I'm a trainer/coach who helps people to drive a car more relaxed, without fear and more confident.

It's a one to one training. I do train people in their own car. It gets people their freedom back to go where and when they like to go by own car...

Target Market(s)

People (man an woman) who are afraid of driving a car, or are very stressed while driving....

Industry/Entity Type

Life Coaching

Font styles to use
Sans Serif

Colors
acd136

Requirements
Must have
• Page 1:
• -my offer (see text-pdf)
• -three fotos (see attached files "Pixmarra") of people who are satisfied with my offer
• Page 2:
• -advantages in the work with me.
• -contact information
• -and a picture of me (see attached file) next to the contact information or the advantages of my work
• -my logo (see attached file) on Page 1 + 2
• -i like a "clear" and structured layout. "Less is more"

```html
<!DOCTYPE html>
<html lang="de">
<head>
<meta charset="utf-8">
<title>Fahrangst Coaching – Flyer</title>
<link href="https://fonts.googleapis.com/css2?family=Oswald:wght@500&family=Lato:ital,wght@0,400;0,700;1,400;1,700&display=swap" rel="stylesheet">
<style>
:root{
  --green:#5cc04a;
  --green-light:#7fd36a;
  --ink:#222222;
  --dark:#1f1f1f;
  --paper:#f4f4f4;
  --paper-shade:#e2e2e2;
  --stage:#d6d6d6;
}
*{margin:0;padding:0;box-sizing:border-box}
html,body{width:1200px;height:1200px;overflow:hidden;background:var(--stage)}
body{position:relative;font-family:'Lato',sans-serif;color:var(--ink)}
.flyer{position:absolute;top:193px;width:484px;height:967px;transform-origin:0 0;transform:scale(.857);
  background:linear-gradient(180deg,var(--paper) 0%,#ffffff 45%,var(--paper-shade) 100%);overflow:hidden}
.flyer--front{left:125px}
.flyer--back{left:661px}
.shapes{position:absolute;inset:0;width:484px;height:967px}
.abs{position:absolute}
.headline{font-family:'Oswald',sans-serif;font-weight:500;text-transform:uppercase;line-height:1.05;letter-spacing:-.3px}
.hero-title{left:34px;top:24px;font-size:38px;color:var(--green)}
.hero-questions{left:34px;top:72px;font-size:15px;line-height:19px}
.tag{font-family:'Oswald',sans-serif;font-weight:500;font-size:18px;text-transform:uppercase;height:36px;line-height:36px;padding-left:25px;letter-spacing:-.2px}
.tag--green{background:var(--green);color:var(--ink);clip-path:polygon(0 0,100% 0,94% 100%,0 100%)}
.tag--dark{background:var(--dark);color:#fff;clip-path:polygon(0 0,93% 0,100% 100%,0 100%)}
.lead{left:26px;top:390px;font-size:15px;font-weight:700}
.bullets{list-style:none;font-size:12.5px;font-style:italic;line-height:16px}
.bullets li{position:relative;padding-left:14px;margin-bottom:17px}
.bullets li::before{content:"";position:absolute;left:0;top:5px;width:6px;height:6px;border-radius:50%;background:var(--green)}
.bullets b{font-weight:700}
.steps{left:25px;top:738px;width:330px;font-size:12.5px;font-style:italic;line-height:16px}
.steps .steps-title{color:var(--green);margin-bottom:7px}
.steps p{margin-bottom:7px}
.footer{left:0;top:913px;width:484px;height:54px;background:var(--dark);color:#fff;font-size:13.5px;line-height:54px}
.footer--front{clip-path:polygon(0 0,290px 0,330px 100%,0 100%);padding-left:32px}
.footer--back{text-align:center}
.contact-name{left:37px;top:26px;font-size:32px;color:#fff}
.contact-info{left:37px;top:106px;font-size:13px;font-weight:700;color:#fff;line-height:16px}
.contact-phone{left:37px;top:174px;font-size:15px;color:#fff;font-family:'Oswald',sans-serif;font-weight:500}
.brand{left:65px;top:815px;color:var(--green);font-family:'Lato',sans-serif;font-weight:400;font-size:22px;line-height:28px}
</style>
</head>
<body>

<!-- Front page -->
<section class="flyer flyer--front">
  <svg class="shapes" viewBox="0 0 484 967" aria-hidden="true">
    <polygon points="228,0 248,0 436,133 412,133" fill="var(--dark)"/>
    <polygon points="248,0 484,0 484,133 436,133" fill="var(--green-light)"/>
    <polygon points="484,420 484,950 410,950" fill="var(--dark)"/>
    <polygon points="484,440 484,950 335,950 440,700" fill="var(--green)"/>
    <rect x="0" y="309" width="484" height="5" fill="var(--dark)"/>
  </svg>
  <svg class="shapes" viewBox="0 0 484 967">
    <polygon role="img" aria-label="Foto: lächelnde Fahrerin am offenen Autofenster" points="0,143 285,143 222,308 0,308" fill="#b7a98a"/>
    <polygon role="img" aria-label="Foto: Fahrerin im Cabrio" points="290,143 484,143 484,308 228,308" fill="#8c8470"/>
    <polygon points="278,665 462,665 445,755 262,755" fill="#ffffff"/>
    <polygon role="img" aria-label="Foto: gelber Kleinwagen auf einer Wiese" points="283,670 456,670 440,750 268,750" fill="#a9b866"/>
  </svg>

  <h1 class="abs headline hero-title">Wollen Sie</h1>
  <p class="abs hero-questions">Fahrangst überwinden?<br>Panikattacken beim Autofahren loswerden?<br>Oder einfach sicher Autofahren?</p>

  <div class="abs tag tag--green" style="left:0;top:337px;width:238px">Dann sind Sie hier richtig!</div>
  <p class="abs lead">Kommt Ihnen eine dieser Situationen bekannt vor?</p>
  <ul class="abs bullets" style="left:26px;top:425px;width:385px">
    <li><b>Angst oder Panikattacken</b> begleiten Sie <b>beim Autofahren</b>. Vielleicht vermeiden Sie deshalb das Autofahren komplett. - Sie möchten angstfrei und/oder ohne Panikattacken fahren.</li>
    <li>Sie <b>trauen sich das Autofahren nicht (mehr) zu</b>. - Sie wünschen sich, sicher, entspannt und stressfrei Auto zu fahren</li>
    <li><b>Autofahren</b> erleben Sie unter <b>hoher Anspannung und Stress</b>. - Sie wünschen sich, Autofahren sicher und entspannt zu erleben.</li>
    <li>Bestimmte Situationen (z.B. <b>Autobahn, Baustellen, Stadtvekehr</b>..) bereiten Ihnen <b>großen Stress</b>. - Sie möchten diese Situationen souveräner meistern.</li>
  </ul>

  <div class="abs tag tag--green" style="left:0;top:674px;width:258px;padding-left:33px">Das muss nicht so bleiben!</div>
  <div class="abs steps">
    <p class="steps-title">3 Schritte zur Lösung:</p>
    <p>1. Erstgespräch vereinbaren</p>
    <p>2. Analyse Ihrer individuellen Situation und Zielsetzung</p>
    <p style="margin-bottom:0"><b>3. Individuelles Coaching und Training</b></p>
    <p>(ggf. Fahrangst-Therapie - als psychotherapeutische Heilpraktikerin bin ich auf Angst- und Panikstörungen spezialisiert)</p>
  </div>

  <div class="abs footer footer--front">www.sicher-fahren-coach.de</div>
</section>

<!-- Back page -->
<section class="flyer flyer--back">
  <svg class="shapes" viewBox="0 0 484 967">
    <polygon role="img" aria-label="Porträtfoto der Trainerin" points="292,0 484,0 484,213 208,213" fill="#cfcfd1"/>
    <polygon points="0,0 276,0 192,213 0,213" fill="var(--green)"/>
    <polygon points="276,0 292,0 208,213 192,213" fill="var(--dark)"/>
    <polygon points="398,195 420,195 484,520 484,560" fill="var(--dark)"/>
    <polygon points="420,195 484,195 484,520" fill="var(--green)"/>
    <rect x="44" y="575" width="402" height="217" fill="var(--green)"/>
    <rect role="img" aria-label="Foto: junges Paar fährt entspannt im Auto" x="47" y="578" width="396" height="211" fill="#9c8f7c"/>
  </svg>

  <h2 class="abs headline contact-name">Katrin<br>Lehmann</h2>
  <p class="abs contact-info">Weitere Informationen<br>finden Sie auf:<br>Oder rufen Sie mich<br>einfach an:</p>
  <p class="abs contact-phone">TEL. 0150 12 34 56 78</p>

  <div class="abs tag tag--dark" style="left:0;top:243px;width:318px;padding-left:39px">Advantages in the work with me</div>
  <ul class="abs bullets" style="left:38px;top:300px;width:385px">
    <li>über 10 Jahre Erfahrung als Trainerin und Coach im Bereich Fahrsicherheit.</li>
    <li>Als psychotherapeutische Heilpraktikerin bin ich auf Angststörungen und Panikattacken spezialisiert</li>
    <li>100 % auf Sie zugeschnitten: ich hole Sie genau dort ab, wo Sie jetzt stehen und unterstütze Sie in Ihrem Prozess individuell und zielführend.</li>
    <li>Wenn es Ihnen nicht möglich ist, in meine Praxis nach Lindenfeld Nord zu kommen: Mit der mobilen Praxis komme ich auch zu Ihnen.</li>
    <li>Termine sind auch abends und am Wochenende möglich.</li>
  </ul>

  <div class="abs brand">
    <div>Katrin Lehmann</div>
    <div>Fahrangst-Coach</div>
  </div>

  <div class="abs footer footer--back">www.sicher-fahren-coach.de</div>
</section>

</body>
</html>
```